vault key finders.com

we are a new company that offer people that have lost there bit coin transaction a recovery and retrieval service
We are looking for a website that will allow you to fill in your details

name
email
bitcoins or other crypto lost and date of transaction

and then an auto reply to them from a given email to verify there email

I am looking for an easy for the client to leave there interest and has a security look around it and looks familiar to the user.

https://purserestore.example/?ref=Xq7LmT2vNp9RsK4wYb8ZcD1fGh6JkM3nQe5UtV0aBy

https://pursemendingaid.example

https://www.zennoro.example/faq-items/restoring-your-token-purse/

Target Market(s)

early investors into crypto

Industry/Entity Type

It Company

Logo Text

VAULTKEY FINDERS/LOCATORS

Coding

Coded - Design and coding required

Number of Pages Required

3 page

Requirements
Must have
• be able to :
• complete
• Name,
• Email
• transaction date of exchange and how much they invested

```html
<!DOCTYPE html>
<html lang="en">
<head>
<meta charset="utf-8">
<title>VaultKey Finders – Retrieve Your Coins</title>
<link rel="stylesheet" href="https://fonts.googleapis.com/css2?family=Poppins:wght@400;500;600;700&display=swap">
<style>
  :root{
    --purple:#9b5ae0;
    --purple-deep:#8a4fd6;
    --sky:#5ec4ec;
    --sky-soft:#b9e1f5;
    --navy:#0c2a44;
    --navy-deep:#071a2c;
    --ink:#1d1d1d;
    --muted:#555;
    --white:#ffffff;
    --footer:#121314;
    --field:#8a8a8a;
  }
  *{box-sizing:border-box;margin:0;padding:0}
  html,body{width:1200px;height:2612px;overflow:hidden;background:var(--white)}
  body{font-family:"Poppins",sans-serif;color:var(--ink);position:relative}
  .page{position:relative;width:1200px;height:2612px}

  /* Hero */
  .hero{position:absolute;left:0;top:0;width:1200px;height:592px}
  .hero-art{position:absolute;inset:0;
    background:radial-gradient(ellipse at 50% 35%,#1b5e86 0%,#0f3a5c 40%,var(--navy-deep) 100%)}
  .brand{position:absolute;left:104px;top:24px;display:flex;align-items:center;gap:14px}
  .brand-mark{width:58px;height:58px;border-radius:50%;background:var(--purple)}
  .brand-name{color:var(--white);font-weight:600;font-size:22px;line-height:26px;letter-spacing:.5px}
  .main-nav{position:absolute;top:45px;left:0;width:1200px}
  .main-nav a{position:absolute;color:var(--white);text-decoration:none;font-weight:600;font-size:16px}
  .hero-title{position:absolute;top:222px;width:1200px;text-align:center;color:var(--white);font-weight:600;font-size:48px}
  .hero-sub{position:absolute;top:286px;width:1200px;text-align:center;color:var(--white);font-weight:500;font-size:29px;line-height:40px}
  .btn{display:inline-flex;align-items:center;justify-content:center;gap:8px;background:linear-gradient(#62c6ee,#3aa8d8);color:var(--white);font-weight:600;text-decoration:none;border:none;font-family:inherit}
  .hero-cta{position:absolute;left:503px;top:381px;width:194px;height:58px;font-size:17px}

  /* About */
  .about-wave{position:absolute;left:0;top:592px;width:1200px;height:500px}
  .about-title{position:absolute;top:668px;width:1200px;text-align:center;color:var(--white);font-weight:500;font-size:34px}
  .about-shadow{position:absolute;left:197px;top:760px;width:842px;height:204px;background:linear-gradient(90deg,#d2c2f3,#c6e4f7);opacity:.9}
  .about-card{position:absolute;left:179px;top:742px;width:842px;height:206px;background:var(--white);box-shadow:0 4px 14px rgba(0,0,0,.15);text-align:center;padding:38px 36px 0}
  .about-card p{font-size:13.5px;line-height:24px;color:var(--muted)}
  .read-more{display:inline-block;margin-top:12px;color:var(--purple);font-size:15px;text-decoration:underline}

  /* How it works */
  .how-title{position:absolute;top:1038px;width:1200px;text-align:center;font-weight:500;font-size:34px}
  .how-intro{position:absolute;left:250px;top:1100px;width:700px;text-align:center;font-size:13.5px;line-height:26px;color:var(--muted)}
  .step{position:absolute}
  .step-icon{position:absolute;width:98px;height:98px;border-radius:50%;background:var(--purple);display:flex;align-items:center;justify-content:center}
  .step-arrow{position:absolute;height:14px}
  .step-text{position:absolute;width:420px}
  .step-text h3{font-weight:500;font-size:22px;margin-bottom:6px}
  .step-text p{font-size:13.5px;line-height:25px;color:var(--muted)}

  /* Contact */
  .contact-art{position:absolute;left:0;top:1780px;width:1200px;height:671px;
    background:radial-gradient(ellipse at 30% 40%,#1e4a66 0%,#13334b 50%,#0a1d2d 100%)}
  .contact-title{position:absolute;left:98px;top:1955px;color:var(--white);font-weight:500;font-size:33px;line-height:45px}
  .contact-copy{position:absolute;left:98px;top:2060px;width:500px;color:#e4ecf2;font-size:15px;line-height:26px}
  .social{position:absolute;top:2193px;width:66px;height:66px;border-radius:50%}
  .social-a{left:103px;background:#3b5ca8}
  .social-b{left:179px;background:#c6262a}
  .social-c{left:256px;background:#3fa9e6}
  .form-card{position:absolute;left:648px;top:1874px;width:453px;height:492px;background:var(--white);padding:40px 35px 0}
  .form-card label{display:block;color:var(--purple);font-size:15px;line-height:22px;font-weight:500}
  .field{display:flex;align-items:center;justify-content:space-between;width:381px;height:35px;border:1px solid var(--field);margin:8px 0 26px;padding:0 14px;font-size:13px;color:#888;font-family:inherit;background:var(--white)}
  .submit{position:absolute;left:286px;top:411px;width:130px;height:39px;font-size:15px}

  /* Footer */
  .site-footer{position:absolute;left:0;top:2451px;width:1200px;height:161px;background:var(--footer)}
  .foot-nav{position:absolute;top:28px;width:1200px;text-align:center;color:var(--white);font-size:15.5px;font-weight:500}
  .foot-nav a{color:var(--white);text-decoration:none;margin:0 22px}
  .foot-rule{position:absolute;left:104px;top:84px;width:995px;height:1px;background:#6a6a6a}
  .copyright{position:absolute;top:106px;width:1200px;text-align:center;color:#ddd;font-size:13px}
</style>
</head>
<body>
<div class="page">

  <header class="hero">
    <div class="hero-art" role="img" aria-label="Blue digital world map with glowing connected coin nodes"></div>
    <div class="brand">
      <span class="brand-mark"></span>
      <span class="brand-name">VAULTKEY<br>FINDERS</span>
    </div>
    <nav class="main-nav">
      <a href="#" style="left:510px">Home</a>
      <a href="#" style="left:601px">About Us</a>
      <a href="#" style="left:716px">Wallets</a>
      <a href="#" style="left:820px">Transfers</a>
      <a href="#" style="left:937px">FAQ</a>
      <a href="#" style="left:1010px">Contact Us</a>
    </nav>
    <h1 class="hero-title">Retrieve Your Bitcoins To The Wallet</h1>
    <p class="hero-sub">Praesent Quis Elementum Urna. Morbi Tincidunt<br>Malesuada Turpis, Ut Dosit Eget.</p>
    <a href="#" class="btn hero-cta">Join Us Now
      <svg width="15" height="15" viewBox="0 0 16 16"><circle cx="8" cy="8" r="8" fill="#fff"/><path d="M6 4l4 4-4 4" stroke="#3aa8d8" stroke-width="2" fill="none"/></svg>
    </a>
  </header>

  <section class="about">
    <svg class="about-wave" viewBox="0 0 1200 500" preserveAspectRatio="none">
      <defs>
        <linearGradient id="aboutGrad" x1="0" y1="1" x2="1" y2="0">
          <stop offset="0" stop-color="#5ec4ec"/>
          <stop offset=".55" stop-color="#8a7fe4"/>
          <stop offset="1" stop-color="#9b5ae0"/>
        </linearGradient>
      </defs>
      <path d="M0 0H1200V244C1080 300 960 330 820 360C600 400 420 330 260 400C150 450 80 480 0 497Z" fill="url(#aboutGrad)"/>
    </svg>
    <h2 class="about-title">ABOUT US</h2>
    <div class="about-shadow"></div>
    <div class="about-card">
      <p>Praesent quis elementum urna. Morbi tincidunt malesuada turpis, ut tristique ipsum porttitor eget. Cras non nibh eget risus pulvinar finibus nec vitae sapien. Integer nisl leo, mollis ac tortor non, placerat pharetra ante. Nunc a cidunt lorem, vitae imperdiet purus. Nunc ac ipsum sit amet libero tristique fringilla. Aliquam commodo, magna scelerisque rutrum pretium, libegna. Suspendisse in tempus velit.</p>
      <a href="#" class="read-more">Read More &#9654;</a>
    </div>
  </section>

  <section class="how">
    <h2 class="how-title">HOW IT WORKS</h2>
    <p class="how-intro">Nunc a cidunt lorem, vitae imperdiet purus. Nunc ac ipsum sit amet libero tristique fringilla. Aliquam commodo, magna scelerisque rutrum pretium, libegna. Suspendisse in tempus velit.</p>

    <!-- step 1 -->
    <div class="step-icon" style="left:204px;top:1210px">
      <svg width="54" height="40" viewBox="0 0 54 40" fill="none" stroke="#fff" stroke-width="2.5"><rect x="2" y="2" width="50" height="36"/><path d="M2 2l25 20 25-20M2 38l18-16M52 38L34 22"/></svg>
    </div>
    <svg class="step-arrow" style="left:322px;top:1252px" width="112" height="14"><line x1="0" y1="7" x2="100" y2="7" stroke="#5ec4ec" stroke-width="2" stroke-dasharray="5 4"/><path d="M98 1l12 6-12 6z" fill="#5ec4ec"/></svg>
    <div class="step-text" style="left:449px;top:1218px">
      <h3>Contact Us</h3>
      <p>Nunc a cidunt lorem, vitae imperdiet purus. Nunc ac ipsum sit amet libero tristique fringilla. Aliquam commodo.</p>
    </div>

    <!-- step 2 -->
    <div class="step-text" style="left:348px;top:1347px">
      <h3>Fill Up The Necessary Details</h3>
      <p>Nunc a cidunt lorem, vitae imperdiet purus. Nunc ac ipsum sit amet libero tristique fringilla. Aliquam commodo.</p>
    </div>
    <svg class="step-arrow" style="left:768px;top:1381px" width="112" height="14"><path d="M14 1L2 7l12 6z" fill="#5ec4ec"/><line x1="12" y1="7" x2="112" y2="7" stroke="#5ec4ec" stroke-width="2" stroke-dasharray="5 4"/></svg>
    <div class="step-icon" style="left:897px;top:1339px">
      <svg width="46" height="52" viewBox="0 0 46 52" fill="none" stroke="#fff" stroke-width="2.5"><path d="M4 2h28v48H4z"/><path d="M10 12h16M10 20h16M10 28h12M10 36h8"/><path d="M42 20L28 42l-4 4 1-6 14-22z"/></svg>
    </div>

    <!-- step 3 -->
    <div class="step-icon" style="left:204px;top:1468px">
      <svg width="56" height="42" viewBox="0 0 56 42" fill="none" stroke="#fff" stroke-width="2.5"><rect x="2" y="2" width="44" height="38" rx="4"/><path d="M46 14h8v14h-8" /><circle cx="50" cy="21" r="1.5" fill="#fff"/><path d="M8 8h30" stroke-dasharray="3 3"/></svg>
    </div>
    <svg class="step-arrow" style="left:322px;top:1510px" width="112" height="14"><line x1="0" y1="7" x2="100" y2="7" stroke="#5ec4ec" stroke-width="2" stroke-dasharray="5 4"/><path d="M98 1l12 6-12 6z" fill="#5ec4ec"/></svg>
    <div class="step-text" style="left:449px;top:1476px">
      <h3>Get Your Coin Back To The Wallet</h3>
      <p>Nunc a cidunt lorem, vitae imperdiet purus. Nunc ac ipsum sit amet libero tristique fringilla. Aliquam commodo.</p>
    </div>

    <!-- step 4 -->
    <div class="step-text" style="left:348px;top:1604px">
      <h3>Pay Us Finally</h3>
      <p>Nunc a cidunt lorem, vitae imperdiet purus. Nunc ac ipsum sit amet libero tristique fringilla. Aliquam commodo.</p>
    </div>
    <svg class="step-arrow" style="left:768px;top:1638px" width="112" height="14"><path d="M14 1L2 7l12 6z" fill="#5ec4ec"/><line x1="12" y1="7" x2="112" y2="7" stroke="#5ec4ec" stroke-width="2" stroke-dasharray="5 4"/></svg>
    <div class="step-icon" style="left:897px;top:1596px">
      <svg width="54" height="46" viewBox="0 0 54 46" fill="none" stroke="#fff" stroke-width="2.5"><circle cx="22" cy="12" r="9"/><path d="M2 34h12l10 6h14l14-12-4-3-12 8H26M14 34l8-6h12"/></svg>
    </div>
  </section>

  <section class="contact">
    <div class="contact-art" role="img" aria-label="Dark city skyline overlaid with a glowing network of connected nodes"></div>
    <h2 class="contact-title">CONTACT US AND RETRIEVE<br>YOUR COINS FASTER</h2>
    <p class="contact-copy">Praesent quis elementum urna. Morbi tincidunt malesuada turpis, ut tristique ipsum porttitor eget. Cras non nibh eget risus pulvinar finibus nec vitae sapien. Integer nisl leo, mollis ac tortor non, placerat pharetra ante. Nunc a cidunt lorem.</p>
    <a href="#" class="social social-a" aria-label="Social profile one"></a>
    <a href="#" class="social social-b" aria-label="Social profile two"></a>
    <a href="#" class="social social-c" aria-label="Social profile three"></a>

    <form class="form-card">
      <label>Name :</label>
      <div class="field"></div>
      <label>Email :</label>
      <div class="field"></div>
      <label>Which Cryptocurrency Are You Trying<br>To Recover?</label>
      <div class="field"><span>Select</span>
        <svg width="12" height="8" viewBox="0 0 12 8"><path d="M0 0h12L6 7z" fill="#666"/></svg>
      </div>
      <label>Date Of Transaction :</label>
      <div class="field"><span>dd - mm - yyyy</span>
        <svg width="14" height="14" viewBox="0 0 14 14" fill="none" stroke="#777" stroke-width="1.5"><rect x="1" y="2" width="12" height="11"/><path d="M1 5h12M4 0v3M10 0v3"/></svg>
      </div>
      <button type="button" class="btn submit">Submit
        <svg width="14" height="14" viewBox="0 0 16 16"><circle cx="8" cy="8" r="8" fill="#fff"/><path d="M6 4l4 4-4 4" stroke="#3aa8d8" stroke-width="2" fill="none"/></svg>
      </button>
    </form>
  </section>

  <footer class="site-footer">
    <nav class="foot-nav">
      <a href="#">Home</a>|<a href="#">About Us</a>|<a href="#">Wallets</a>|<a href="#">Transfers</a>|<a href="#">FAQ</a>|<a href="#">Contact Us</a>
    </nav>
    <div class="foot-rule"></div>
    <p class="copyright">Copyright © 2018. All Rights Reserved.</p>
  </footer>

</div>
</body>
</html>
```